Business Card Design

I need a business card for a new company based in Australia called "MedLinkora".

Its a cloud program for GPs that allows them to search for the specialist they require using a simple user friendly tool.

I would like the colours to match those in the program (the colours in the logo attached).

The final design should reflect the programs clarity, ease of use and professionalism.

Target Market(s)

GPs and other Health Professionals

Industry/Entity Type

Business

Contact Information for Business Card

MedLinkora; The Trusted Clinician Index; Marla Ostrove CEO; 0438215906; marla@medlinkora.example; www.medlinkora.example

Requirements
Must have
• Must have the logo attached; the web address and my name and phone number
Nice to have
• the slogan "The Trusted Clinician Index"

```html
<!DOCTYPE html>
<html lang="en">
<head>
<meta charset="utf-8">
<title>MedLinkora Business Card</title>
<link rel="stylesheet" href="https://fonts.googleapis.com/css2?family=Open+Sans:wght@300;400;600;700&display=swap">
<style>
  :root {
    --brand-blue: #1cb2e4;
    --ink: #2e2e2e;
    --muted: #8a8a8a;
    --paper: #ffffff;
    --backdrop: #ecebea;
  }
  * { box-sizing: border-box; margin: 0; padding: 0; }
  html, body {
    width: 1200px;
    height: 829px;
    overflow: hidden;
    background: var(--backdrop);
    font-family: "Open Sans", Arial, sans-serif;
  }
  .sheet {
    position: relative;
    width: 1200px;
    height: 829px;
  }
  .card {
    position: absolute;
    top: 264px;
    width: 520px;
    height: 300px;
    box-shadow: 0 2px 10px rgba(0,0,0,0.12);
  }
  .card--front { left: 60px; background: var(--paper); }
  .card--back  { left: 620px; background: var(--brand-blue); color: var(--paper); }

  /* Front */
  .brand {
    position: absolute;
    left: 34px;
    top: 40px;
  }
  .brand__name {
    font-size: 46px;
    font-weight: 400;
    line-height: 1;
    letter-spacing: -1px;
    color: var(--brand-blue);
  }
  .brand__tagline {
    margin-top: 4px;
    font-size: 15px;
    font-weight: 400;
    color: var(--muted);
    letter-spacing: 0.3px;
  }
  .person {
    position: absolute;
    right: 34px;
    top: 52px;
    text-align: right;
  }
  .person__name {
    font-size: 14px;
    font-weight: 700;
    color: var(--brand-blue);
  }
  .person__role {
    font-size: 10px;
    color: var(--muted);
    margin-top: 1px;
  }
  .contacts {
    position: absolute;
    left: 34px;
    bottom: 40px;
    list-style: none;
  }
  .contacts__item {
    display: flex;
    align-items: center;
    gap: 9px;
    font-size: 15px;
    color: var(--ink);
    line-height: 1;
    margin-top: 9px;
  }
  .contacts__icon { width: 16px; height: 16px; flex: none; }

  /* Back */
  .back-brand {
    position: absolute;
    left: 0;
    right: 0;
    top: 92px;
    text-align: center;
  }
  .back-brand__name {
    font-size: 58px;
    font-weight: 400;
    line-height: 1;
    letter-spacing: -1px;
  }
  .back-brand__tagline {
    margin-top: 6px;
    font-size: 18px;
    letter-spacing: 0.3px;
  }
  .back-web {
    position: absolute;
    left: 0;
    right: 0;
    top: 208px;
    text-align: center;
    font-size: 16px;
    letter-spacing: 2px;
  }
</style>
</head>
<body>
<main class="sheet">

  <section class="card card--front" aria-label="Business card front">
    <div class="brand">
      <div class="brand__name">MedLinkora</div>
      <div class="brand__tagline">The Trusted Clinician Index</div>
    </div>

    <div class="person">
      <div class="person__name">Marla Ostrove</div>
      <div class="person__role">CEO</div>
    </div>

    <ul class="contacts">
      <li class="contacts__item">
        <svg class="contacts__icon" viewBox="0 0 16 16" aria-hidden="true">
          <circle cx="8" cy="8" r="8" fill="var(--brand-blue)"/>
          <path d="M5.3 4.2l1.3 1.6-.7 1a5 5 0 0 0 2.9 2.9l1-.7 1.6 1.3-.6 1.3c-3.6 0-6.7-3.1-6.7-6.7z" fill="#fff"/>
        </svg>
        <span>0438215906</span>
      </li>
      <li class="contacts__item">
        <svg class="contacts__icon" viewBox="0 0 16 16" aria-hidden="true">
          <circle cx="8" cy="8" r="8" fill="var(--brand-blue)"/>
          <rect x="4" y="5.2" width="8" height="5.6" fill="#fff"/>
          <path d="M4 5.2l4 3 4-3" fill="none" stroke="var(--brand-blue)" stroke-width="0.9"/>
        </svg>
        <span>marla@medlinkora.example</span>
      </li>
      <li class="contacts__item">
        <svg class="contacts__icon" viewBox="0 0 16 16" aria-hidden="true">
          <circle cx="8" cy="8" r="8" fill="var(--brand-blue)"/>
          <g fill="none" stroke="#fff" stroke-width="0.9">
            <circle cx="8" cy="8" r="4.2"/>
            <ellipse cx="8" cy="8" rx="1.8" ry="4.2"/>
            <path d="M3.8 8h8.4M4.4 6h7.2M4.4 10h7.2"/>
          </g>
        </svg>
        <span>www.medlinkora.example</span>
      </li>
    </ul>
  </section>

  <section class="card card--back" aria-label="Business card back">
    <div class="back-brand">
      <div class="back-brand__name">MedLinkora</div>
      <div class="back-brand__tagline">The Trusted Clinician Index</div>
    </div>
    <div class="back-web">www.medlinkora.example</div>
  </section>

</main>
</body>
</html>
```